I'd like a business card that makes my company, Harwick Denton Associates Ltd stand out from the normal financial & IT services sector . It would be great to have a card that a potential client will think "wow" this is out of the norm , I'll give these guys a call. My business aims to provide consultancy services for financial and IT institutions but I'm looking to provide a newer approach that fits into today's social media rather than the standard "big 4" approach. My business helps companies assess their internal issues and aims to solve issues via business process re-engineering. The final design should have a balance of the maturity of the financial & IT sector with the fresh approach of the thriving social media sector

Target Market(s)

Business Managers and Directors, technical Managers and directors. Aged between 20 and 60 that handle project budgets

Industry/Entity Type

Financial

Requirements
Must have
• Must incorporate company logo currently being designed
Should not have
• No old-style fonts please.

```html
<!DOCTYPE html>
<html lang="en">
<head>
<meta charset="utf-8">
<title>Harwick Denton Associates Ltd – Business Card</title>
<link href="https://fonts.googleapis.com/css2?family=Open+Sans:wght@400;600;700&display=swap" rel="stylesheet">
<style>
  :root {
    --page-bg: #e6e7ea;
    --card-bg: #fbfbfb;
    --ink: #2b2b2d;
    --ink-soft: #3a3a3c;
    --brand-blue: #2f6fd0;
    --brand-blue-light: #1b8fdc;
    --brand-blue-deep: #2a58b8;
    --line-dark: #232325;
  }
  html, body {
    margin: 0;
    width: 1200px;
    height: 901px;
    overflow: hidden;
    background: var(--page-bg);
  }
  .business-card {
    position: absolute;
    left: 100px;
    top: 165px;
    width: 1000px;
    height: 572px;
    border-radius: 48px;
    background: var(--card-bg);
    overflow: hidden;
    box-shadow: 0 10px 30px rgba(0,0,0,0.15);
    font-family: "Open Sans", Arial, sans-serif;
    color: var(--ink);
  }
  .card-swoosh {
    position: absolute;
    inset: 0;
    width: 100%;
    height: 100%;
  }
  .company-name {
    position: absolute;
    left: 64px;
    top: 44px;
    margin: 0;
    font-weight: 700;
    font-size: 40px;
    line-height: 1.12;
    letter-spacing: 3px;
    text-transform: uppercase;
    color: var(--ink);
  }
  .contact-block {
    position: absolute;
    right: 56px;
    top: 150px;
    text-align: right;
  }
  .person-name {
    margin: 0;
    font-size: 30px;
    font-weight: 400;
    color: var(--ink);
  }
  .person-title {
    margin: 2px 0 0;
    font-size: 21px;
    color: var(--ink-soft);
  }
  .address {
    margin: 48px 0 0;
    font-size: 16px;
    line-height: 1.45;
    color: var(--ink-soft);
  }
  .contact-list {
    list-style: none;
    margin: 36px 0 0;
    padding: 0;
    font-size: 17px;
    line-height: 1.6;
    color: var(--ink-soft);
  }
  .contact-list li {
    display: flex;
    justify-content: flex-end;
    align-items: center;
    gap: 10px;
  }
  .contact-icon {
    width: 15px;
    height: 15px;
    fill: var(--ink);
  }
</style>
</head>
<body>
  <article class="business-card">
    <svg class="card-swoosh" viewBox="0 0 1000 572" preserveAspectRatio="none" aria-hidden="true">
      <defs>
        <linearGradient id="swooshBlue" x1="0" y1="0" x2="1" y2="0">
          <stop offset="0" stop-color="var(--brand-blue-deep)"/>
          <stop offset="0.55" stop-color="var(--brand-blue-light)"/>
          <stop offset="1" stop-color="var(--brand-blue)"/>
        </linearGradient>
      </defs>
      <path d="M0,245 C150,370 450,572 1000,585 L1000,600 L0,600 Z" fill="url(#swooshBlue)"/>
      <path d="M0,215 C150,340 450,545 1000,560" fill="none" stroke="var(--line-dark)" stroke-width="5"/>
    </svg>

    <h1 class="company-name">Harwick Denton<br>Associates Ltd</h1>

    <section class="contact-block">
      <p class="person-name">Daniel Harker</p>
      <p class="person-title">President</p>
      <p class="address">041.12th floor,Quay<br>Harbour Road HDN</p>
      <ul class="contact-list">
        <li>020 481 7352
          <svg class="contact-icon" viewBox="0 0 16 16"><path d="M3.5 1.5l2.5 3-1.5 1.5c.8 2 2.5 3.7 4.5 4.5L10.5 9l3 2.5-1.5 2.5C7 14 2 9 2 3z"/></svg>
        </li>
        <li>020 481 7353
          <svg class="contact-icon" viewBox="0 0 16 16"><path d="M4.5 1h7v14h-7zM6 2.5v9.5h4V2.5z"/><circle cx="8" cy="13.5" r=".8" fill="#fff"/></svg>
        </li>
        <li>020 481 7354
          <svg class="contact-icon" viewBox="0 0 16 16"><path d="M4 1h6l2 2v4H4zM2 7h12v6h-2v2H4v-2H2zM5.5 11v2.5h5V11z"/></svg>
        </li>
        <li>daniel@hdassoc.com
          <svg class="contact-icon" viewBox="0 0 16 16"><path d="M1 3.5h14v9H1zM2.5 5v.3L8 9l5.5-3.7V5L8 8.5z"/></svg>
        </li>
        <li>www.hdassociates.com
          <svg class="contact-icon" viewBox="0 0 16 16"><circle cx="8" cy="8" r="6.5" fill="none" stroke="var(--ink)" stroke-width="1.4"/><ellipse cx="8" cy="8" rx="2.8" ry="6.5" fill="none" stroke="var(--ink)" stroke-width="1.2"/><path d="M1.5 8h13" stroke="var(--ink)" stroke-width="1.2"/></svg>
        </li>
      </ul>
    </section>
  </article>
</body>
</html>
```